NetStar Trust Brochure -- tri-fold

I need a logo design and brochure layout for a new fund I've established to support girls who are interested in participating in volleyball, but lack the funds to pay full price. The brochure will be used to raise money for the fund. I've attached a description of the fund's goals and requirements for distribution to help describe what we do. Feel free to use as much or as little as you wish. I look forward to receiving your ideas!

LATE NOTE: I've seen many awesome submissions, but I want to acknowledge that the I realize if we use all the copy I provided, it will be suffocating to the reader. So, please feel free to design and include whatever text you think would be most compelling to a target contributor.

Target Market(s)

Parent donors to the fund

Industry/Entity Type

It Support

Logo Text

NetStar Trust

Font styles to use
Serif
Sans Serif

Colors
0255a3
ecf7fb

Requirements
Must have
• Contact: netstartrust@mailbrook.example or Margaret Tolliver at 5478810396
• Colors are navy and silver -- UPDATE this was tough to select from the color wheel below so I did my best, but navy and traditional silver are definite
• Donations are not tax deductible
Nice to have
• Our mission:
• * Provide financial support to pre-high school volleyball players who are committed to volleyball, but lack the financial support necessary to participate in the program to which they have been accepted.
• * Seek dedicated athletes who are willing to invest in their future participation in volleyball either through direct financial participation or volunteer opportunities or both to further their futures in volleyball.
• *Reward players who recognize that participation in volleyball is an opportunity as well as a commitment and are dedicated to adhering to the expectations of the team to which they are invited to join, and becoming a positive leader and contributor to the team.

```html
<!DOCTYPE html>
<html lang="en">
<head>
<meta charset="utf-8">
<title>NetStar Trust Brochure</title>
<link rel="stylesheet" href="https://fonts.googleapis.com/css2?family=Raleway:wght@300;400&display=swap">
<style>
  :root {
    --navy: #0255a3;
    --panel-blue: #0d5aa7;
    --ice: #ecf7fb;
    --silver: #b9bec4;
    --ink: #2a2a2a;
    --white: #ffffff;
  }
  * { margin: 0; padding: 0; box-sizing: border-box; }
  html, body {
    width: 1200px; height: 770px; overflow: hidden;
    background: var(--white);
    font-family: "Raleway", Arial, sans-serif;
  }
  .spread {
    position: absolute; left: 18px; top: 93px;
    width: 1163px; height: 581px;
    display: flex;
  }
  .intro-panel {
    width: 353px; height: 100%;
    background: var(--ice);
    padding: 125px 0 0 48px;
    position: relative;
  }
  .brand {
    display: flex; align-items: center; gap: 8px;
    margin-bottom: 9px;
  }
  .brand-dot {
    width: 14px; height: 14px; border-radius: 50%;
    background: var(--silver); flex: none;
  }
  .fund-name {
    font-weight: 300; font-size: 25px; color: var(--navy);
    letter-spacing: -0.5px; line-height: 30px;
  }
  .hook {
    font-weight: 300; font-size: 12.6px; line-height: 15px;
    color: var(--navy); letter-spacing: -0.45px;
    width: 272px; margin-bottom: 6px;
  }
  .hook-answer {
    font-weight: 300; font-size: 12.6px; color: var(--ink);
    letter-spacing: -0.45px; margin: 2px 0 14px;
  }
  .why {
    font-weight: 300; font-size: 9.2px; line-height: 15.5px;
    color: var(--ink); letter-spacing: -0.35px; width: 270px;
    margin-bottom: 16px;
  }
  .contact {
    position: absolute; left: 48px; bottom: 28px; width: 270px;
    border-top: 1px solid var(--silver); padding-top: 9px;
    font-weight: 300; font-size: 9.2px; line-height: 14px;
    color: var(--ink); letter-spacing: -0.2px;
  }
  .contact-label { color: var(--navy); font-weight: 400; }
  .tax-note { margin-top: 4px; font-style: normal; color: var(--navy); }
  .accent-strip { width: 28px; height: 100%; background: var(--panel-blue); }
  .player-photo {
    width: 201px; height: 100%;
    background: linear-gradient(180deg, #d9d7cf 0%, #c9c6bc 45%, #8a8f97 62%, #9b8362 85%, #7d6444 100%);
  }
  .details-panel {
    flex: 1; height: 100%;
    background: var(--panel-blue); color: var(--white);
    padding: 52px 0 0 88px;
  }
  .details-lead {
    font-size: 12px; line-height: 14px; width: 404px; margin-bottom: 14px;
    letter-spacing: -0.1px;
  }
  .criteria { list-style: none; width: 404px; }
  .criteria li {
    position: relative; padding-left: 14px;
    font-size: 12px; line-height: 14px; margin-bottom: 6px;
    letter-spacing: -0.1px;
  }
  .criteria li::before {
    content: "•"; position: absolute; left: 0; top: 0; font-size: 9px;
  }
  .criteria li.tight { margin-bottom: 1px; }
</style>
</head>
<body>
  <main class="spread">
    <section class="intro-panel">
      <div class="brand">
        <span class="brand-dot"></span>
        <h1 class="fund-name">NetStar Trust</h1>
      </div>
      <p class="hook">Do you or someone you know love to fly through the air and smack a ball to the ground?</p>
      <p class="hook">Do they enjoy diving to the ground to stop a ball from landing?</p>
      <p class="hook">Do they relish being part of a team and working together towards a common goal?</p>
      <p class="hook">Do they want to stay active 365 days a year inside and out of doors?</p>
      <p class="hook-answer">If so, it's likely that they love volleyball!</p>
      <p class="why">Volleyball is a great sport for many reasons. It's fast paced, it challenges players to jump higher, move more quickly, get stronger, communicate better, and actively contribute to the betterment of their team in a proactive and positive manner.</p>
      <p class="why">But, it can also be expensive....</p>
      <address class="contact">
        <span class="contact-label">Contact:</span> netstartrust@mailbrook.example<br>
        or Margaret Tolliver at 5478810396
        <p class="tax-note">Donations are not tax deductible.</p>
      </address>
    </section>
    <div class="accent-strip"></div>
    <div class="player-photo" role="img" aria-label="Smiling volleyball player in a dark number 12 uniform holding a ball overhead in a gym"></div>
    <section class="details-panel">
      <p class="details-lead">The 2015 Cedar Ridge North Varsity Volleyball players established the NetStar Trust to support pre-high school aged girls who want to play volleyball, but may lack the financial support required to participate in camps or competitive teams.&nbsp; The fund has distributed an average of $500 per year to athletes who meet the following qualifications:</p>
      <ul class="criteria">
        <li>Demonstrated financial need – a written statement from a parent or guardian concerning financial constraints is sufficient though additional information or documentation may be requested at the discretion of the Fund.</li>
        <li>Player contribution – each player is expected to invest in her volleyball experience. Players must provide a description of the monetary commitment they are willing to make to their volleyball experience. Players are encouraged to explore a variety of avenues to achieve this goal including</li>
        <li>Paid opportunities such as babysitting, lawn work, light housekeeping, retail and other external paid employment;</li>
        <li>Volunteer hours at local charities focused on athletics for girls and young adults or volleyball camps run by local middle and high schools (hours must meet or exceed 20 hours per period for which contribution is requested and be verified by supervisor)</li>
        <li>Other opportunities based upon prior evaluation and acceptance from the Fund</li>
        <li class="tight">Coach's recommendation – a written statement from the team's coach or administrator confirming the applicant's invitation to join the team and estimated costs to participate.</li>
        <li>Player commitment – each player must agree to meet the expectations of the team to which financial assistance is dedicated by the Fund. Players will be expected to sign a commitment notice evidencing their agreement to abide by the team's rules and expectations. Failure to adhere to this requirement will result in revocation of any financial assistance and eligibility for future support from the Fund.</li>
      </ul>
    </section>
  </main>
</body>
</html>
```